Brisk Lark Delivery Service Wordpress design

My client is a delivery service whose motto is "We go where the freight leads us." Their colors are red, white and blue. They use Voyara vans and box vans - NO semi tractors. They like this Website design www.kwuzo.com, but I would like to see some designs that make them stand out. Attached is their new logo.

Target Market(s)

Businesses who use delivery services in town and anyone needing freight picked up or transported in the United States.

Industry/Entity Type

Delivery Service

Number of Pages Required

1 page

Font styles to use
Sans Serif

Colors
ec1f27
0455a3
ffffff

Requirements
Must have
• We need a Wordpress design with sliders that incorporates their new logo and the motto "WE GO WHERE THE FREIGHT LEADS US" Their corporate colors are red, white and blue. They only use voyara vans and box vans.
Nice to have
• Please use your creativity to come up with a unique design for this delivery service.
Should not have
• NO SEMI TRACTOR TRAILERS

```html
<!DOCTYPE html>
<html lang="en">
<head>
<meta charset="utf-8">
<title>Brisk Lark Delivery Service</title>
<link href="https://fonts.googleapis.com/css2?family=Exo+2:wght@400;500;600&family=Arimo:wght@400;700&display=swap" rel="stylesheet">
<style>
:root{
  --navy:#201c6c;
  --navy-deep:#17145a;
  --navy-light:#2e2b92;
  --red:#ec1f27;
  --white:#ffffff;
  --grey:#9a9a9a;
  --grey-dark:#666666;
  --head:"Exo 2", sans-serif;
  --body:"Arimo", sans-serif;
}
*{margin:0;padding:0;box-sizing:border-box}
html,body{width:1200px;height:2510px;overflow:hidden;background:var(--white)}
body{position:relative;font-family:var(--body);color:var(--grey-dark)}
.abs{position:absolute}

/* top bar */
.top-bar{left:0;top:0;width:1200px;height:52px;background:var(--navy);display:flex;justify-content:flex-end;align-items:center;gap:34px;padding-right:80px;color:var(--white);font-family:var(--head);font-size:16px;font-weight:500}
.top-bar span{display:flex;align-items:center;gap:10px}

/* header */
.site-header{left:0;top:52px;width:1200px;height:114px;background:var(--white)}
.brand{left:77px;top:38px}
.brand-name{font-family:var(--head);font-weight:600;font-size:32px;color:var(--red);letter-spacing:1px;line-height:1}
.main-nav{right:80px;top:46px;display:flex;gap:40px;font-family:var(--head);font-size:16px;font-weight:500;color:#444}
.main-nav .active{color:var(--navy)}

/* hero */
.hero{left:0;top:166px;width:1200px;height:520px;background:radial-gradient(ellipse at center,var(--navy-light) 0%,var(--navy) 60%,var(--navy-deep) 100%)}
.slide-frame{left:77px;top:48px;width:1046px;height:427px;background:var(--white);padding:12px;box-shadow:0 0 30px rgba(0,0,0,.4)}
.slide-photo{width:100%;height:100%;background:linear-gradient(180deg,#6f9ec9 0%,#a9c7df 30%,#e9ecef 55%,#8c8a6a 78%,#3d3d36 100%)}
.slide-caption{left:23px;top:134px;width:486px;height:181px;background:rgba(255,255,255,.72);padding:32px 18px;font-family:var(--head);font-weight:500;font-size:47px;line-height:58px;color:var(--red)}
.slider-dots{left:0;top:491px;width:1200px;display:flex;justify-content:center;gap:8px}
.slider-dots i{width:11px;height:11px;border-radius:50%;background:var(--white)}
.slider-dots i.on{background:var(--red)}

/* service cards */
.service-card{top:750px;width:333px;height:218px;box-shadow:0 14px 14px -10px rgba(0,0,0,.35)}
.service-photo{width:333px;height:166px}
.service-label{position:absolute;left:0;bottom:0;width:333px;height:52px;background:rgba(32,28,108,.9);display:flex;align-items:center;justify-content:space-between;padding:0 14px;font-family:var(--head);font-weight:500;font-size:18px;color:var(--white)}

/* welcome */
.welcome-title{left:0;top:1088px;width:1200px;text-align:center;font-family:var(--head);font-weight:500;font-size:40px;color:var(--navy)}
.welcome-title span,.news-title span{color:var(--red)}
.welcome-text{left:130px;top:1150px;width:940px;text-align:center;font-size:14.5px;line-height:29.5px;color:var(--grey)}
.btn-more{left:517px;top:1247px;width:166px;height:62px;background:var(--red);color:var(--white);border-radius:3px;display:flex;align-items:center;justify-content:center;font-family:var(--head);font-weight:500;font-size:19px}

/* vehicles */
.vehicles{left:0;top:1373px;width:1200px;height:207px;background:var(--navy)}
.vehicle-text{font-family:var(--body);font-size:14.5px;line-height:29px;color:var(--white)}
.vehicle-title{font-family:var(--head);font-weight:500;font-size:34px;color:var(--white);margin-bottom:12px;line-height:1}

/* news */
.news-title{left:0;top:1636px;width:1200px;text-align:center;font-family:var(--head);font-weight:500;font-size:40px;color:var(--navy)}
.news-item{top:1712px;width:333px}
.news-photo{width:333px;height:208px;box-shadow:0 12px 12px -10px rgba(0,0,0,.35)}
.news-head{margin-top:20px;font-family:var(--head);font-weight:500;font-size:18.5px;line-height:28px;color:var(--navy);text-transform:uppercase}
.news-date{margin-top:6px;font-family:var(--head);font-size:15px;color:var(--red)}
.news-body{margin-top:8px;width:310px;font-size:14.5px;line-height:29px;color:var(--grey)}

/* footer */
.site-footer{left:0;top:2178px;width:1200px;height:269px;background:var(--navy);color:var(--white)}
.foot-col{top:34px}
.foot-heading{font-family:var(--head);font-weight:500;font-size:17px;margin-bottom:22px;letter-spacing:.5px}
.foot-text{font-size:14.5px;line-height:28px;width:235px}
.foot-links{list-style:disc;padding-left:22px;font-size:13.5px;line-height:27px}
.contact-row{display:flex;gap:14px;font-size:13.5px;line-height:22px;margin-bottom:12px}
.social{display:flex;gap:10px;margin-top:18px}
.social i{width:34px;height:34px;border-radius:50%;background:var(--white)}
.newsletter-box{margin-top:16px;width:249px;height:40px;border:1px solid var(--white);border-radius:3px;display:flex;align-items:center;justify-content:space-between;padding:0 16px;font-size:13.5px}
.copyright{left:0;top:2447px;width:1200px;height:63px;background:var(--navy-deep);color:var(--white);display:flex;align-items:center;justify-content:center;font-size:14px}
</style>
</head>
<body>

<div class="abs top-bar">
  <span><svg width="16" height="16" viewBox="0 0 24 24" fill="#fff"><path d="M6.6 10.8a15 15 0 0 0 6.6 6.6l2.2-2.2c.3-.3.7-.4 1-.2 1.1.4 2.3.6 3.6.6.6 0 1 .4 1 1V20c0 .6-.4 1-1 1A17 17 0 0 1 3 4c0-.6.4-1 1-1h3.5c.6 0 1 .4 1 1 0 1.3.2 2.5.6 3.6.1.3 0 .7-.2 1z"/></svg>+1 555 014 2290</span>
  <span><svg width="14" height="16" viewBox="0 0 14 16" fill="#fff"><circle cx="7" cy="4" r="4"/><path d="M0 16c0-4 3-7 7-7s7 3 7 7z"/></svg>CUSTOMER LOGIN</span>
</div>

<header class="abs site-header">
  <div class="abs brand"><div class="brand-name">BRISK LARK</div></div>
  <nav class="abs main-nav">
    <span class="active">HOME</span><span>ABOUT</span><span>SERVICES</span><span>COURIER</span><span>CAREERS</span><span>CONTACT</span>
  </nav>
</header>

<section class="abs hero">
  <div class="abs slide-frame">
    <div class="slide-photo" role="img" aria-label="White delivery van on a country road with a smiling courier carrying a parcel"></div>
    <div class="abs slide-caption">WE GO WHERE THE FREIGHT LEADS US</div>
  </div>
  <div class="abs slider-dots"><i></i><i></i><i class="on"></i><i></i><i></i></div>
</section>

<section>
  <div class="abs service-card" style="left:77px">
    <div class="service-photo" role="img" aria-label="Courier delivering boxes at a front door" style="background:linear-gradient(160deg,#d9cfc0,#8c7a60 55%,#4a6fa8)"></div>
    <div class="service-label">EXPRESS COURIER<svg width="18" height="16" viewBox="0 0 18 16" fill="none" stroke="#ec1f27" stroke-width="2.5"><path d="M2 2l6 6-6 6M9 2l6 6-6 6"/></svg></div>
  </div>
  <div class="abs service-card" style="left:434px">
    <div class="service-photo" role="img" aria-label="Passenger in a wheelchair being assisted onto a van lift" style="background:linear-gradient(160deg,#6b6a55,#4a4a48 50%,#9a9ea3)"></div>
    <div class="service-label">MEDICAL ADVANTAGE<svg width="18" height="16" viewBox="0 0 18 16" fill="none" stroke="#ec1f27" stroke-width="2.5"><path d="M2 2l6 6-6 6M9 2l6 6-6 6"/></svg></div>
  </div>
  <div class="abs service-card" style="left:790px">
    <div class="service-photo" role="img" aria-label="Row of white freight vans parked in a yard" style="background:linear-gradient(180deg,#b8c8d8,#e6eaee 50%,#9a9c9a)"></div>
    <div class="service-label">EXPRESS FREIGHT<svg width="18" height="16" viewBox="0 0 18 16" fill="none" stroke="#ec1f27" stroke-width="2.5"><path d="M2 2l6 6-6 6M9 2l6 6-6 6"/></svg></div>
  </div>
</section>

<section>
  <h1 class="abs welcome-title">WELCOME TO <span>BRISK LARK</span></h1>
  <p class="abs welcome-text">Lorem Ipsum is simply dummy text of the printing and typesetting industry. Lorem Ipsum has been the industry's standard dummy text ever since the 1500s, when an unknown printer took a galley of type and scrambled it to make a type specimen book. It has survived not only five centuries, but also the leap into</p>
  <div class="abs btn-more">KNOW MORE</div>
</section>

<section class="abs vehicles">
  <svg class="abs" style="left:0;top:0" width="600" height="207"><polygon points="0,0 586,0 560,207 0,207" fill="#ec1f27"/></svg>
  <div class="abs" role="img" aria-label="White box van" style="left:0;top:67px;width:214px;height:128px;background:linear-gradient(180deg,#f4f4f4,#d8d8d8 70%,#555);border-radius:6px 20px 10px 6px"></div>
  <div class="abs" style="left:251px;top:42px">
    <h2 class="vehicle-title">BOX VAN</h2>
    <p class="vehicle-text">Lorem Ipsum is simply dummy text of<br>the printing and typesetting industry.<br>Lorem Ipsum has been the.</p>
  </div>
  <div class="abs" style="left:609px;top:42px">
    <h2 class="vehicle-title">VOYARA VANS</h2>
    <p class="vehicle-text" style="text-align:center">Lorem Ipsum is simply dummy text of<br>the printing and typesetting industry.<br>Lorem Ipsum has been the.</p>
  </div>
  <div class="abs" role="img" aria-label="White high-roof cargo van" style="left:929px;top:8px;width:271px;height:193px;background:linear-gradient(180deg,#fafafa,#e2e2e2 65%,#444);border-radius:40px 8px 10px 14px"></div>
</section>

<section>
  <h2 class="abs news-title">LATEST <span>NEWS</span></h2>
  <article class="abs news-item" style="left:77px">
    <div class="news-photo" role="img" aria-label="Courier handing a parcel to a customer" style="background:linear-gradient(120deg,#2f5db0,#dcd4c8 55%,#f3efe9)"></div>
    <h3 class="news-head">Lorm ipsum is simple text of printing and typesetting.</h3>
    <div class="news-date">17 June 2016</div>
    <p class="news-body">Lorem Ipsum is simply dummy text of the printing and typesetting industry. Lorem Ipsum has been the industry's</p>
  </article>
  <article class="abs news-item" style="left:434px">
    <div class="news-photo" role="img" aria-label="Two movers unloading a box from a van" style="background:linear-gradient(120deg,#e8e8e6,#2a4d8f 50%,#8a9a7a)"></div>
    <h3 class="news-head">Lorm ipsum is simple text of printing and typesetting.</h3>
    <div class="news-date">17 June 2016</div>
    <p class="news-body">Lorem Ipsum is simply dummy text of the printing and typesetting industry. Lorem Ipsum has been the industry's</p>
  </article>
  <article class="abs news-item" style="left:790px">
    <div class="news-photo" role="img" aria-label="Parcel being passed between two people at a doorway" style="background:linear-gradient(120deg,#cfe0c0,#b08a58 50%,#6a3a50)"></div>
    <h3 class="news-head">Lorm ipsum is simple text of printing and typesetting.</h3>
    <div class="news-date">17 June 2016</div>
    <p class="news-body">Lorem Ipsum is simply dummy text of the printing and typesetting industry. Lorem Ipsum has been the industry's</p>
  </article>
</section>

<footer class="abs site-footer">
  <div class="abs foot-col" style="left:77px;top:36px;width:245px">
    <div class="brand-name" style="font-size:22px;margin-bottom:36px">BRISK LARK</div>
    <p class="foot-text">Lorem Ipsum is simply dummy text of the printing and typesetting industry. Lorem Ipsum.</p>
    <div class="social"><i></i><i></i><i></i><i></i></div>
  </div>
  <div class="abs foot-col" style="left:345px">
    <div class="foot-heading">USEFULL LINKS</div>
    <ul class="foot-links"><li>Home</li><li>About</li><li>Services</li><li>Courier</li><li>Careear</li><li>Contact</li></ul>
  </div>
  <div class="abs foot-col" style="left:608px;width:230px">
    <div class="foot-heading">GET IN TOUCH</div>
    <div class="contact-row"><svg width="16" height="20" viewBox="0 0 16 20" fill="none" stroke="#fff" stroke-width="1.5" style="flex:none"><path d="M8 19s7-7 7-11A7 7 0 0 0 1 8c0 4 7 11 7 11z"/><circle cx="8" cy="8" r="2.5"/></svg><div>BRISK LARK<br>Lorem ipsum is simple dummy text of printing and type.</div></div>
    <div class="contact-row"><svg width="16" height="16" viewBox="0 0 24 24" fill="none" stroke="#fff" stroke-width="2"><path d="M6.6 10.8a15 15 0 0 0 6.6 6.6l2.2-2.2c.3-.3.7-.4 1-.2 1.1.4 2.3.6 3.6.6.6 0 1 .4 1 1V20c0 .6-.4 1-1 1A17 17 0 0 1 3 4c0-.6.4-1 1-1h3.5c.6 0 1 .4 1 1 0 1.3.2 2.5.6 3.6.1.3 0 .7-.2 1z"/></svg><div>555 - 014 - 2291</div></div>
    <div class="contact-row"><svg width="16" height="14" viewBox="0 0 16 12" fill="none" stroke="#fff" stroke-width="1.5"><rect x="1" y="1" width="14" height="10"/><path d="M1 1l7 6 7-6"/></svg><div>info@brisklark.com</div></div>
  </div>
  <div class="abs foot-col" style="left:874px;width:250px">
    <div class="foot-heading">NEWSLETTER</div>
    <p style="font-size:13px;line-height:22px;width:225px">Subscribe to Our Newsletter to get Latest Updates &amp; news</p>
    <div class="newsletter-box"><span>Type Your E-mail:</span><svg width="14" height="12" viewBox="0 0 14 12" fill="#fff"><path d="M0 5h9V1l5 5-5 5V7H0z"/></svg></div>
  </div>
</footer>
<div class="abs copyright">©Brisk Lark - 2016 All rights reserved.</div>

</body>
</html>
```